Cruise Booking Website

Cruise search and booking website

This project is a redesign of a cruise booking website we did a few years ago.

The current website is located here: http://voyage.pixelmarsh.com/en/

It's not fully functional but gives you ad idea how miserable the old design was.

All the information about cruises, cruise lines, destinations, ports and shore excursions will be similar to http://www.sailorbay.com/
Actual search pages (form, results, single result, sailing and cabin selection, ship info, booking) will have EXACTLY the same info as sailorbay.com

We like the style of http://harborvoyagehub.com, it's quite modern, good spacing, not overloaded with information. So you can use it as an example of what we like, not what we want as a final result for us. Please, don't copy it. The result should not be possible to resemble the harborvoyagehub.com, because our site has to be unique. This is important!
If you submit a design that clearly reminds another cruise site it will be rejected!

Also the mockup provided is just to give you the basic structure and show what information has to be present on the page. It doesn't mean the layout has to be the same as a mockup. The layout is up to the designer.

I've updated the mockup to be more generic so it doesn't confuse you:
https://www.filecrate.net/s/k7q2mz9pw4tnb3x/Home%20page.png

When you're adding social sharing icons like chatterbox/peeplet you have to use chinese ones instead:
https://www.filecrate.net/s/h3rt8wyd6jcl0fe/chinese-social-icons.png
Originals: http://shrtlk.example/qRmT

We'll start with home page first and after it's approved inner pages can be designed.

I know the cost of the project doesn't look high, but the task is straight forward and doesn't require to be very original, it's better to follow existing design and layout patterns that proved to work well.
That's why I encourage you to choose a template to build the design on top of one of https://themequarry.net/ themes if it will save the design work, will be easier and faster for you. So it will be more like a customization than a new design from scratch.

Mockups, site map and logo files:
- https://www.filecrate.net/sh/50xb7vq1ndtpkez/RmwuHp8Zq3

Website tree:
- https://papers.quillnet.example/document/d/8vTrXk2MqLpZ4wNsB7yHcE1oUjFgD9aR_QbVtnWm/edit?usp=sharing
Updates

So far a lot of designs are just copying http://www.harborvoyagehub.com/ - we don't like it!

We like the style of harborvoyagehub.com, it's quite modern, good spacing, not overloaded with information. So you can use it as an example of what we like, not what we want as a final result for us. Please, don't copy it. The result should not be possible to resemble the harborvoyagehub.com, because our site has to be unique. This is important!

Target Market(s)

Chinese travellers

Industry/Entity Type

Build

Requirements
Must have
• * White, blue and red
* Large spacing, not too much information cramped into a small space like sailorbay.com or the current website
* More "hidden" info in popups, tabs and so on, so not to many things are visible at the same time
* Compatible with lumen framekit styling (for easier coding):
- http://lumenkit.example.io/framework/index.html
- http://skinvault.net/
* Feel free to propose to build the design on top of one of https://themequarry.net/ themes if it will save the design work, will be easier and faster for you

```html
<!DOCTYPE html>
<html lang="en">
<head>
<meta charset="utf-8">
<title>蓝航邮轮 – Cruise Booking</title>
<link href="https://fonts.googleapis.com/css2?family=Open+Sans:wght@400;600;700;800&display=swap" rel="stylesheet">
<style>
:root{
  --navy:#143e72;
  --blue:#2470b8;
  --blue-light:#3d8ed6;
  --red:#e03a3a;
  --red-dark:#c22b2b;
  --ink:#333a42;
  --muted:#7a828c;
  --line:#d9dee5;
  --pale:#eef1f5;
  --panel:#474c53;
  --footer:#3a3d42;
  --footer-deep:#2b2d31;
  --white:#ffffff;
}
*{box-sizing:border-box;margin:0;padding:0}
html,body{width:798px;height:1200px;overflow:hidden}
body{font-family:"Open Sans",Arial,sans-serif;color:var(--ink);background:var(--white);position:relative;font-size:9px;line-height:1.4}
.abs{position:absolute}

/* header */
.site-header{left:0;top:0;width:798px;height:48px;background:linear-gradient(90deg,#0f3561,#1d5a94 55%,#12406f)}
.brand{left:22px;top:9px;display:flex;align-items:center;gap:8px;color:var(--white);font-weight:800;font-size:22px;letter-spacing:1px}
.brand-dot{width:26px;height:26px;border-radius:50%;background:var(--white)}
.search-box{left:470px;top:9px;display:flex}
.search-box input{width:150px;height:18px;border:0;border-radius:2px 0 0 2px;padding:0 6px;font:inherit;font-size:8px}
.search-box span{height:18px;padding:0 8px;background:var(--blue-light);color:#fff;font-weight:700;font-size:8px;line-height:18px;border-radius:0 2px 2px 0}
.adv-search{left:540px;top:30px;color:#cfe2f6;font-size:7.5px;text-decoration:underline}
.account-links{left:676px;top:6px;width:106px;list-style:none}
.account-links li{color:#fff;font-size:7.5px;font-weight:700;text-transform:uppercase;border-bottom:1px solid rgba(255,255,255,.25);padding:1px 0 1px 4px}

/* nav */
.main-nav{left:0;top:48px;width:798px;height:32px;background:linear-gradient(#3b8bd4,#1f66ad);display:flex;align-items:center;padding-left:40px;border-bottom:2px solid var(--navy)}
.main-nav a{color:#fff;text-decoration:none;font-size:8.5px;font-weight:700;text-transform:uppercase;padding:0 11px;border-right:1px solid rgba(255,255,255,.3);display:flex;align-items:center;gap:4px}
.main-nav a:last-of-type{border-right:0}
.nav-home{margin-left:auto;margin-right:40px;width:22px;height:22px;display:flex;align-items:center;justify-content:center}

/* hero */
.hero{left:0;top:80px;width:798px;height:266px;background:linear-gradient(180deg,#7fb5df 0%,#a9d0ee 35%,#3d7fb8 62%,#1c4f86 100%)}
.hero-photo{left:0;top:0;width:798px;height:266px}
.hero-title{left:80px;top:30px;color:#fff;font-size:27px;font-weight:700;letter-spacing:1px}
.hero-box{left:80px;top:84px;width:250px;padding:10px 12px;background:rgba(24,92,168,.85);color:#fff;font-size:8.5px;line-height:1.5}
.hero-badge{left:318px;top:140px;width:62px;height:62px;border-radius:50%;background:var(--red);color:#fff;font-weight:800;font-size:9px;text-align:center;display:flex;align-items:center;justify-content:center;line-height:1.1;border:2px solid #fff}
.hero-arrow{top:112px;width:24px;height:40px;background:rgba(20,40,70,.6);display:flex;align-items:center;justify-content:center}

/* utility row */
.hotline{left:40px;top:362px;width:196px;height:32px;border:1px solid var(--red);display:flex;align-items:center;gap:8px;padding:0 8px;font-size:11px;font-weight:700;color:var(--red)}
.hotline small{color:var(--ink);font-weight:600;font-size:9px}
.btn-account{top:366px;height:24px;padding:0 12px;background:var(--blue);color:#fff;font-size:8px;font-weight:700;display:flex;align-items:center;gap:5px;border-radius:2px;text-transform:uppercase}

/* finder */
.finder{left:566px;top:352px;width:192px;height:196px;background:var(--panel);padding:10px;color:#fff}
.finder h3{font-size:10px;font-weight:700;text-transform:uppercase;margin-bottom:6px}
.finder .field{height:15px;background:#fff;color:var(--ink);font-size:7.5px;padding:0 5px;line-height:15px;margin-bottom:5px;border-radius:1px;display:flex;justify-content:space-between}
.finder .label{font-size:7.5px;font-weight:600;margin:3px 0 3px}
.finder .pair{display:flex;gap:6px}
.finder .pair .field{flex:1}
.finder .check{display:flex;align-items:center;gap:4px;font-size:7.5px;margin:2px 0 7px}
.finder .check i{width:8px;height:8px;background:#fff;display:block}
.finder .go{background:var(--red);text-align:center;font-weight:700;font-size:8.5px;height:18px;line-height:18px;border-radius:2px}

/* feature tiles */
.tile{top:414px;width:160px}
.tile-photo{height:82px}
.tile h4{font-size:9.5px;font-weight:600;margin:5px 0 3px}
.read-more{display:inline-flex;align-items:center;gap:4px;font-size:7.5px;color:var(--ink)}
.read-more b{width:10px;height:10px;background:var(--red);display:block;border-radius:1px}

/* info columns */
.info{top:590px;width:224px}
.info-icon{width:84px;height:84px;border-radius:50%;border:3px solid var(--red);margin:0 auto 16px;display:flex;align-items:center;justify-content:center;color:var(--red);font-weight:800;font-size:13px}
.info h4{font-size:12px;font-weight:700;margin-bottom:4px}
.info p{color:var(--muted);font-size:8.5px;line-height:1.5}
.info p em{font-style:normal;color:var(--blue);font-weight:600}

/* deals */
.deals{left:0;top:806px;width:798px;height:206px;background:var(--pale)}
.deals-title{left:40px;top:814px;width:718px;font-size:18px;color:#4d5560;font-weight:400;border-bottom:1px solid var(--line);padding-bottom:4px}
.deal{top:856px;width:170px;height:146px;background:#fff;border:1px solid var(--line);text-align:center}
.deal-head{height:34px;line-height:34px;font-size:11px;font-weight:600;color:var(--blue);border-bottom:1px solid var(--line)}
.deal-head.filled{background:var(--blue);color:#fff}
.deal p{font-size:8px;color:var(--muted);padding:10px 12px 0;line-height:1.5;height:78px;text-align:left}
.choose{display:inline-block;background:var(--red);color:#fff;font-weight:700;font-size:7.5px;padding:4px 10px;border-radius:2px;text-transform:uppercase}
.deal-list{padding:6px 8px 0;text-align:left;height:82px}
.deal-list div{display:flex;gap:6px;margin-bottom:6px;font-size:7px;color:var(--muted);line-height:1.35}
.deal-list i{flex:0 0 26px;height:22px;background:linear-gradient(#8fc0e6,#2f6ea8)}

/* partners */
.partners{left:0;top:1012px;width:798px;height:54px;background:var(--red);display:flex;align-items:center;padding:0 40px;color:#fff}
.partners h3{font-size:17px;font-weight:400;margin-right:auto}
.partners span{font-size:10px;font-weight:700;margin-left:22px;display:flex;align-items:center;gap:5px}
.partners span i{width:8px;height:8px;background:#fff;display:block}

/* footer */
.site-footer{left:0;top:1066px;width:798px;height:106px;background:var(--footer);display:flex;padding:14px 40px 0 70px;gap:40px}
.site-footer ul{list-style:none}
.site-footer li{color:#cfd3d8;font-size:7.5px;margin-bottom:3px;display:flex;align-items:center;gap:5px}
.site-footer li::before{content:"";width:3px;height:3px;background:var(--red);display:block}
.social{margin-left:auto}
.social li::before{display:none}
.social li i{width:10px;height:10px;border-radius:2px;display:block}
.copyright{left:0;top:1172px;width:798px;height:28px;background:var(--footer-deep);color:#9aa0a7;font-size:7.5px;text-align:center;padding-top:5px;line-height:1.35}
</style>
</head>
<body>

<header class="site-header abs">
  <div class="brand abs"><span class="brand-dot"></span>蓝航邮轮</div>
  <div class="search-box abs"><input type="text" value="Search cruises"><span>Search</span></div>
  <a class="adv-search abs">Advance Search</a>
  <ul class="account-links abs">
    <li>Sign up</li>
    <li>Online booking</li>
    <li>Members centre</li>
  </ul>
</header>

<nav class="main-nav abs">
  <a>Destinations <svg width="6" height="4"><path d="M0 0h6L3 4z" fill="#fff"/></svg></a>
  <a>Cruise Lines <svg width="6" height="4"><path d="M0 0h6L3 4z" fill="#fff"/></svg></a>
  <a>Shore Activities <svg width="6" height="4"><path d="M0 0h6L3 4z" fill="#fff"/></svg></a>
  <a>Promotions <svg width="6" height="4"><path d="M0 0h6L3 4z" fill="#fff"/></svg></a>
  <a>Cruise News <svg width="6" height="4"><path d="M0 0h6L3 4z" fill="#fff"/></svg></a>
  <a>Blog <svg width="6" height="4"><path d="M0 0h6L3 4z" fill="#fff"/></svg></a>
  <a>FAQ(QA)</a>
  <a>Contact Us</a>
  <span class="nav-home"><svg width="14" height="13" viewBox="0 0 14 13"><path d="M7 0L0 6h2v7h4V9h2v4h4V6h2z" fill="#fff"/></svg></span>
</nav>

<section class="hero abs">
  <div class="hero-photo abs" role="img" aria-label="Cruise ship sailing on open sea with a couple on deck"></div>
  <h1 class="hero-title abs">WELCOME TO 蓝航邮轮</h1>
  <p class="hero-box abs">Cruises are offered throughout the world and for each destination there are a number of cruise lines to choose from. From contemporary cruise lines to luxury cruise lines each cruise line offers different itineraries, features and options.</p>
  <div class="hero-badge abs">BEST<br>VALUE</div>
  <span class="hero-arrow abs" style="left:8px"><svg width="8" height="12"><path d="M7 1L2 6l5 5" stroke="#fff" stroke-width="2" fill="none"/></svg></span>
  <span class="hero-arrow abs" style="left:766px"><svg width="8" height="12"><path d="M1 1l5 5-5 5" stroke="#fff" stroke-width="2" fill="none"/></svg></span>
</section>

<div class="hotline abs">
  <svg width="16" height="16" viewBox="0 0 16 16"><path d="M3 1l3 3-2 2c1 2 3 4 6 6l2-2 3 3-2 2C7 15 1 9 1 3z" fill="#e03a3a"/></svg>
  <small>Hotline:</small> 4008 512 330
</div>
<div class="btn-account abs" style="left:300px"><svg width="9" height="9"><circle cx="4.5" cy="3" r="2.5" fill="#fff"/><path d="M0 9c0-3 9-3 9 0z" fill="#fff"/></svg>Register</div>
<div class="btn-account abs" style="left:392px"><svg width="9" height="9"><rect x="1" y="3" width="7" height="6" fill="#fff"/><path d="M2.5 3V2a2 2 0 014 0v1" stroke="#fff" fill="none"/></svg>My Account</div>

<form class="finder abs">
  <h3>Find your cruise</h3>
  <div class="field">Any Destination <span>▾</span></div>
  <div class="field">Any Cruise Line <span>▾</span></div>
  <div class="field">Any Month <span>▾</span></div>
  <div class="field">Any Length <span>▾</span></div>
  <div class="label">Number of Travelers</div>
  <div class="pair"><div class="field">2 Adults <span>▾</span></div><div class="field">0 Kids <span>▾</span></div></div>
  <div class="check"><i></i>Check for Senior Rates</div>
  <div class="go">SEARCH</div>
</form>

<article class="tile abs" style="left:40px">
  <div class="tile-photo" role="img" aria-label="Large cruise ship at sea" style="background:linear-gradient(#9cc8ea,#2e6fa8)"></div>
  <h4>Cruise lines</h4>
  <span class="read-more"><b></b>Read More</span>
</article>
<article class="tile abs" style="left:212px">
  <div class="tile-photo" role="img" aria-label="Harbour town with ships moored along the shore" style="background:linear-gradient(#a8d2ef,#5b8e6c)"></div>
  <h4>Shore Activities</h4>
  <span class="read-more"><b></b>Read More</span>
</article>
<article class="tile abs" style="left:384px">
  <div class="tile-photo" role="img" aria-label="Cruise ship docked beside a city skyline" style="background:linear-gradient(#b7d6ee,#4a78a0)"></div>
  <h4>Cruise news</h4>
  <span class="read-more"><b></b>Read More</span>
</article>

<article class="info abs" style="left:40px">
  <div class="info-icon">BLOG</div>
  <h4>Blog</h4>
  <p>Read stories from our guests and crew, tips on packing, ports worth a longer stop and the best cabins on every ship. New posts arrive each week from the travel team. <em>Learn More »</em></p>
</article>
<article class="info abs" style="left:287px">
  <div class="info-icon"><svg width="30" height="30" viewBox="0 0 30 30"><circle cx="15" cy="15" r="13" fill="none" stroke="#e03a3a" stroke-width="3"/><path d="M11 11a4 4 0 118 0c0 3-4 3-4 6" fill="none" stroke="#e03a3a" stroke-width="3"/><circle cx="15" cy="22" r="1.8" fill="#e03a3a"/></svg></div>
  <h4>FAQ(Q&amp;A)</h4>
  <p>Answers to common questions about visas, payment, boarding, luggage and onboard costs. Cannot find what you need? Our service team replies within one day. <em>Learn More »</em></p>
</article>
<article class="info abs" style="left:534px">
  <div class="info-icon"><svg width="24" height="32" viewBox="0 0 24 32"><path d="M12 1C6 1 2 5 2 11c0 8 10 20 10 20s10-12 10-20C22 5 18 1 12 1z" fill="none" stroke="#e03a3a" stroke-width="3"/><circle cx="12" cy="11" r="4" fill="#e03a3a"/></svg></div>
  <h4>Ports</h4>
  <p>Explore departure and call ports across Asia, Europe and the Americas, with shore guides, local weather and transfer details for each harbour stop. <em>Learn More »</em></p>
</article>

<section class="deals abs"></section>
<h2 class="deals-title abs">Our Deals</h2>

<article class="deal abs" style="left:40px">
  <div class="deal-head">Packages</div>
  <p>lanhang.cn offers the best cruise deals and discounts on all cruise lines and cruise and air packages each week. Learn More »</p>
  <span class="choose">Choose Plan</span>
</article>
<article class="deal abs" style="left:222px">
  <div class="deal-head filled">Recommended</div>
  <p>Let us pick your cruise at ease by answering questions about travel style, trip length and budget. Learn More »</p>
  <span class="choose">Choose Plan</span>
</article>
<article class="deal abs" style="left:404px">
  <div class="deal-head">Last Minute Deals</div>
  <p>Last minute cruises offer great opportunity to get exceptional cruise deals, discounts, upgrades and other valuable offers. Learn More »</p>
  <span class="choose">Choose Plan</span>
</article>
<article class="deal abs" style="left:586px">
  <div class="deal-head filled">Starlane Cruise Deals</div>
  <div class="deal-list">
    <div><i role="img" aria-label="Ship thumbnail"></i>5-Day Sales Event featuring exclusive savings plus onboard credit.</div>
    <div><i role="img" aria-label="Ship thumbnail"></i>FREE complimentary specialty dinner for two on select sailings.</div>
    <div><i role="img" aria-label="Ship thumbnail"></i>Kids sail free this summer.</div>
  </div>
  <span class="choose">Choose Plan</span>
</article>

<section class="partners abs">
  <h3>Our Partners</h3>
  <span><i></i>Nordvale</span>
  <span><i></i>Cortessa</span>
  <span><i></i>Regent Tide</span>
  <span><i></i>Marigold Line</span>
  <span><i></i>Meridia</span>
</section>

<footer class="site-footer abs">
  <ul><li>Visa</li><li>About us</li><li>Contact us</li><li>Payment info</li></ul>
  <ul><li>Terms of privacy</li><li>Terms of service</li><li>Terms of insurance</li><li>Corporate groups</li></ul>
  <ul><li>Registration agreement</li><li>Cruise promotion policy</li><li>Booking process explained</li><li>Bonus points collect policy</li></ul>
  <ul class="social">
    <li><i style="background:#e04a3f"></i>Chatterbox</li>
    <li><i style="background:#2f8fd6"></i>Peeplet</li>
    <li><i style="background:#3aa55d"></i>Ripplemail</li>
    <li><i style="background:#e8a23a"></i>Kiteboard</li>
    <li><i style="background:#6a62c9"></i>Harbourcast</li>
  </ul>
</footer>
<div class="copyright abs">Copyright © 2011 蓝航邮轮 All rights reserved<br>沪ICP备 00000000号</div>

</body>
</html>
```